Tildens Biscuit Barn Website

I need a website for a diner/restaurant that has been established in a farming, oil and industrial community for over 15 years. The website needs to be simple in design, but that should demonstrate the mastery of skills of the designer. Our diner/restaurant is family oriented, patriotic but very rustic
Fb Address is fb.me/TildensBarn

Pictures of the restaurant

https://www.filecrate-example.net/s/qk72hdw01/Tildens_05.jpg

Pictures of About us

https://www.filecrate-example.net/sh/zm40vrt88/AboutUsPhotos

Article about Tilden's
https://www.filecrate-example.net/s/wp31nbx57/TildensBiscuitBarn1.PDF
https://www.filecrate-example.net/s/hy65lcu29/TildensBiscuitBarn2.PDF

Reason: I was slow to update with information.

Reason: I am just getting feedback to the designs posted. I wasn't sure of the limited feedback was limiting designers from submitting designs. That and running a business with 25 employees open 12 hours a day, being here 2 hours prior and 2-3 hours after makes for long days.

I've increased the first place prize and also added funds to the second and third place prizes for your effort.

I just need the files in PSD, not HTML 5 as originally requested. We can handle getting the coding part.

Ill have the contest finalized by Monday. Thanks for your patience.

Target Market(s)

Cross section of adults from 18-35 & 35-55.

Industry/Entity Type

Industrial

Font styles to use
Other font styles liked:
• ff tisa web pro or garamond premier pro

Requirements
Must have
• Must be clean, look nice and not look like an afterthought.
Nice to have
• Please see the last two documents for information about our restaurant, which was featured in our local newspaper.

```html
<!DOCTYPE html>
<html lang="en">
<head>
<meta charset="utf-8">
<title>Tildens Biscuit Barn</title>
<link rel="stylesheet" href="https://fonts.googleapis.com/css2?family=Cinzel+Decorative:wght@400;700&family=Courier+Prime&family=Geo&family=Josefin+Sans:wght@400;600;700&family=Open+Sans:wght@400;700&family=Playfair+Display:ital@1&family=Oswald:wght@500&display=swap">
<style>
  :root {
    --paper: #f1eee8;
    --ink: #5b5b5b;
    --nav-blue: #2f6f86;
    --nav-red: #b5223a;
    --rust: #c0752d;
    --rust-dark: #9a5a22;
    --wine: #8f1e33;
    --gold: #f1d64c;
    --frame: #d9b07a;
    --teal: #2a6479;
    --teal-dark: #1f4f62;
    --map: #6f6c66;
    --card: #ede0c4;
    --white: #ffffff;
  }
  * { margin: 0; padding: 0; box-sizing: border-box; }
  html, body { width: 1200px; height: 3203px; overflow: hidden; }
  body { background: var(--paper); font-family: "Open Sans", sans-serif; color: var(--ink); position: relative; }

  .site-header, .about, .menu, .contact { position: absolute; left: 0; width: 1200px; }

  /* Header */
  .site-header { top: 0; height: 800px; background: var(--paper); }
  .call { position: absolute; left: 100px; top: 70px; display: flex; gap: 14px; align-items: center; color: #9a9a9a; font-family: "Oswald", sans-serif; font-size: 24px; line-height: 1.15; }
  .brand { position: absolute; left: 480px; top: 30px; width: 240px; height: 290px; display: flex; flex-direction: column; align-items: center; justify-content: center; gap: 18px; }
  .brand-dot { width: 150px; height: 150px; border-radius: 50%; background: var(--nav-blue); }
  .brand-name { font-family: "Josefin Sans", sans-serif; font-weight: 700; font-size: 46px; color: var(--nav-red); }
  .nav-rail { position: absolute; top: 210px; height: 48px; border-top: 2px solid #d99aa5; border-bottom: 2px solid #d99aa5; display: flex; align-items: center; font-family: "Oswald", sans-serif; font-size: 24px; color: #a8a8a8; }
  .nav-rail.left { left: 137px; width: 333px; }
  .nav-rail.right { left: 734px; width: 333px; }
  .nav-rail a { position: absolute; text-decoration: none; color: inherit; }
  .nav-rail a.active { color: var(--nav-blue); }
  .nav-arrow { position: absolute; top: 222px; }
  .social-square { position: absolute; left: 1040px; top: 68px; width: 58px; height: 62px; background: #5f6a78; border: 4px solid #c9b48e; }

  .slide { position: absolute; left: 100px; top: 350px; width: 543px; height: 406px; background: linear-gradient(160deg, #c9cfd3 0%, #9aa3a8 45%, #4a4a48 100%); border: 3px solid #2a2a2a; }
  .slide-prev { position: absolute; left: 82px; top: 528px; }
  .welcome { position: absolute; left: 679px; top: 372px; width: 395px; text-align: center; }
  .welcome h1 { font-family: "Cinzel Decorative", serif; font-size: 66px; font-weight: 400; color: #6b6b6b; letter-spacing: 2px; line-height: 90px; }
  .welcome p { margin-top: 16px; font-family: "Josefin Sans", sans-serif; font-size: 13.5px; line-height: 25.6px; text-transform: uppercase; text-align: justify; text-align-last: center; color: #5e5e5e; }
  .like { margin-top: 28px; display: inline-flex; gap: 6px; font-size: 11px; }
  .like span { border: 1px solid #c5c8d0; padding: 2px 6px; background: #f5f6f8; color: #3b5998; }

  /* About */
  .about { top: 800px; height: 801px; background: radial-gradient(ellipse at 50% 45%, #d99a48 0%, var(--rust) 55%, var(--rust-dark) 100%); }
  .about-frame { position: absolute; left: 267px; top: 139px; width: 666px; height: 545px; border: 3px solid var(--frame); padding: 14px; background: rgba(255,235,190,0.25); }
  .about-panel { width: 100%; height: 100%; background: var(--wine); text-align: center; padding: 0 40px; overflow: hidden; }
  .about h2 { font-family: "Geo", sans-serif; font-weight: 400; font-size: 86px; color: var(--gold); padding-top: 22px; line-height: 96px; }
  .about p { font-family: "Josefin Sans", sans-serif; font-size: 12px; line-height: 24px; color: var(--white); text-transform: uppercase; margin-top: 22px; }
  .about p + p { margin-top: 10px; }

  /* Menu */
  .menu { top: 1601px; height: 797px; background: radial-gradient(ellipse at 60% 40%, #33738a 0%, var(--teal) 55%, var(--teal-dark) 100%); }
  .menu h2 { position: absolute; top: 90px; width: 100%; text-align: center; font-family: "Geo", sans-serif; font-weight: 400; font-size: 92px; color: var(--white); }
  .menu-list { position: absolute; top: 240px; list-style: none; font-family: "Courier Prime", monospace; font-size: 26px; color: var(--white); letter-spacing: 1px; }
  .menu-list li { height: 58.5px; }
  .menu-list.left { left: 143px; }
  .menu-list.right { left: 655px; }
  .price { font-family: "Playfair Display", serif; font-style: italic; }

  /* Contact */
  .contact { top: 2398px; height: 805px; background: var(--map); }
  .map-ring { position: absolute; left: 113px; top: 207px; width: 358px; height: 358px; border-radius: 50%; background: #3a3a3a; padding: 16px; }
  .map-lens { width: 100%; height: 100%; border-radius: 50%; background: linear-gradient(180deg, #d8d0b6 0%, #e6d79b 50%, #cfc6ad 100%); }
  .contact h2 { position: absolute; left: 662px; top: 135px; width: 380px; font-family: "Geo", sans-serif; font-weight: 400; font-size: 90px; color: var(--white); white-space: nowrap; }
  .contact-card { position: absolute; left: 668px; top: 249px; width: 368px; height: 342px; background: var(--card); border: 8px solid #c8b892; padding: 32px 36px; font-family: "Courier Prime", monospace; font-size: 20px; line-height: 28px; color: #333; white-space: nowrap; }
  .contact-card .phone { color: var(--nav-red); margin-top: 20px; }
  .contact-card .hours { margin-top: 20px; }
  .find-us { margin-top: 18px; display: inline-flex; align-items: center; gap: 10px; background: #46629e; color: var(--white); font-family: "Courier Prime", monospace; font-size: 16px; line-height: 20px; padding: 12px 14px; white-space: nowrap; }
  .find-us i { width: 22px; height: 22px; background: var(--white); display: block; }
  .copyright { position: absolute; bottom: 20px; width: 100%; text-align: center; font-size: 14px; color: #e3e1dc; }
</style>
</head>
<body>

<header class="site-header">
  <div class="call">
    <svg width="28" height="22" viewBox="0 0 28 22" aria-hidden="true"><path d="M2 6 Q14 -2 26 6 L23 10 L19 8 L19 5 Q14 3 9 5 L9 8 L5 10 Z M7 12 H21 L24 21 H4 Z" fill="#a5a5a5"/></svg>
    <div>Call<br>555 014 2207</div>
  </div>

  <div class="brand">
    <div class="brand-dot"></div>
    <div class="brand-name">Tilden's</div>
  </div>

  <svg class="nav-arrow" style="left:100px" width="20" height="24" viewBox="0 0 20 24" aria-hidden="true"><path d="M16 2 L4 12 L16 22 L12 12 Z" fill="var(--nav-red)"/></svg>
  <nav class="nav-rail left">
    <a class="active" href="#" style="left:35px">HOME</a>
    <a href="#about" style="left:163px">About Us</a>
  </nav>
  <nav class="nav-rail right">
    <a href="#menu" style="left:43px">Menu</a>
    <a href="#contact" style="left:169px">Contact Us</a>
  </nav>
  <svg class="nav-arrow" style="left:1080px" width="20" height="24" viewBox="0 0 20 24" aria-hidden="true"><path d="M4 2 L16 12 L4 22 L8 12 Z" fill="var(--nav-red)"/></svg>

  <div class="social-square"></div>

  <div class="slide" role="img" aria-label="Photo of two guests at a diner table with breakfast plates"></div>
  <svg class="slide-prev" width="44" height="44" viewBox="0 0 44 44" aria-hidden="true"><circle cx="22" cy="22" r="20" fill="#6e6a52" stroke="#d9d2b0" stroke-width="2"/><path d="M25 13 L16 22 L25 31" stroke="#fff" stroke-width="4" fill="none"/></svg>

  <section class="welcome">
    <h1>WELCOME</h1>
    <p>Phasellus et quam nibh. Nullam bibendum libero eros. Pellentesque eu mauris aliquam, volutpat odio in, viverra mauris. Nullam eu velit velit. Mauris ut neque at sapien accumsan suscipit. Sed iaculis commodo lacus, in maximus mauris laoreet ac. In ultrices sem et nisl mattis, et feugiat purus faucibus. Praesent aliquam urna eget porttitor pretium. In fringilla libero quis lorem sollicitudin porttitor. Nunc convallis vel sem vel varius.</p>
    <div class="like"><span>Like</span><span>3k</span></div>
  </section>
</header>

<section class="about" id="about">
  <div style="position:absolute;inset:0" role="img" aria-label="Faint sketched drawing of a coffee cup behind the panel"></div>
  <div class="about-frame">
    <div class="about-panel">
      <h2>ABOUT</h2>
      <p>Phasellus et quam nibh. Nullam bibendum libero eros. Pellentesque eu mauris aliquam, volutpat odio in, viverra mauris. Nullam eu velit velit. Mauris ut neque at sapien accumsan suscipit. Sed iaculis commodo lacus, in maximus mauris laoreet ac. In ultrices sem et nisl mattis, et feugiat purus faucibus. Praesent aliquam urna eget porttitor pretium. In fringilla libero quis lorem sollicitudin porttitor. Nunc convallis vel sem vel varius.</p>
      <p>Praesent accumsan scelerisque rhoncus. Praesent pharetra augue a urna fringilla, vel placerat justo gravida. Suspendisse nec quam augue. Sed sit amet eros non quam blandit lacinia sed at justo. Donec in cursus purus. Nulla facilisi. Vestibulum bibendum placerat vehicula, sed non aliquam enim. Pellentesque magna massa, pretium nec lectus efficitur, egestas vestibulum arcu. Nam fermentum at tellus at accumsan. Vestibulum ante ipsum primis in faucibus orci luctus et ultrices posuere cubilia.</p>
    </div>
  </div>
</section>

<section class="menu" id="menu">
  <div style="position:absolute;inset:0" role="img" aria-label="Dim photo of a breakfast plate, coffee cup and small flag"></div>
  <h2>MENU</h2>
  <ul class="menu-list left">
    <li>Aenean vel = <span class="price">$1</span></li>
    <li>Nam semperege = <span class="price">$2</span></li>
    <li>Duis aliquam nulla = <span class="price">90p</span></li>
    <li>Praesent volutpat = <span class="price">75p</span></li>
    <li>Nam sodales = <span class="price">52p</span></li>
    <li>Etiam posuere tellus = <span class="price">$1</span></li>
    <li>Phasellus et = <span class="price">22p</span></li>
    <li>Proin = <span class="price">$1</span></li>
  </ul>
  <ul class="menu-list right">
    <li>Aenean vel = <span class="price">$1</span></li>
    <li>Nam semperege = <span class="price">$2</span></li>
    <li>Duis aliquam nulla = <span class="price">90p</span></li>
    <li>Praesent volutpat = <span class="price">75p</span></li>
    <li>Nam sodales = <span class="price">52p</span></li>
    <li>Etiam posuere tellus = <span class="price">$1</span></li>
    <li>Phasellus et = <span class="price">22p</span></li>
    <li>Proin = <span class="price">$1</span></li>
  </ul>
</section>

<section class="contact" id="contact">
  <div style="position:absolute;inset:0" role="img" aria-label="Muted street map of the surrounding neighbourhood"></div>
  <div class="map-ring">
    <div class="map-lens" role="img" aria-label="Magnified street map showing the diner location"></div>
  </div>
  <h2>CONTACT US</h2>
  <div class="contact-card">
    <div>Quarry Ridge Rd<br>Millbrook, Ohio</div>
    <div class="phone">+1 555-013-4471</div>
    <div class="hours">Closed Now<br>Today 5:00am – 2:00pm</div>
    <div class="find-us"><i></i>Find us on Friendbook</div>
  </div>
  <div class="copyright">Copyright © 2014 Tildens Biscuit Barn. All rights reserved.</div>
</section>

</body>
</html>
```